We need your help in designing the graphical look of the home page of our web site: Plimora.com.

Plimora is an FREE online service that brings consumers and service providers together through online reservations.

Our service is in fact a web application (similar to quindle planner), so we will be using forms, widgets, menus and standard web controls (buttons, fields, links, etc). We need a design that will be easy to integrate with our programming.

This design project is for the HOME page, but we will choose the designer that will design the web page in photoshop in layers, so we can easily derive our other secondary pages ourselves.

If you have any questions please send us a message and we will gladly update the brief with a response.

Happy Designing!
Updates

Hi all, the menu on the home page should be something standard, like: Pricing, features, how it works.

once a user is logged in, they will see their toolbox at all times:
- My Box (links to their main page of bookings)
- My Faborites (view favorite businesses and book quickly with them)
- Settings (set parameters of their account)

There should be a My Profile page as well. 

Thanks!

Reason: I have extended the deadline to receive more designs.

Hi All,

UPDATE: we changed our vision of the home page to have a much simpler design.  something along the lines of chatterloom peeplark and crew lattice.

HOME PAGE:
light colors with white background.  simple, simple, simple!

header should not be big, logo, change language link. try with search bar (what and where).

body should be simple, with an image + register form only.

footer with links to pages for more info:
- Privacy,
- Getting started
- How it works
- Contact us
- FAQ
- Pricing

LOGGED IN PAGE:
when logged in, the header can be the same or reduced to maximize the "working area" (body).
body can be a 2 or 3 column design, as we have a main working area.  in your design, show a calendar.  we need a toolbar (side or top) that will have these buttons, links: MyBox, My Favorites, Settings, My Profile.
We need a section that will display latest messages or notifications.
keep the footer with the links.

Thank you all.

Reason: Holidays

Reason: holidays... lets spend time with our families!

Target Market(s)

Young and mobile consumers + professionals, businesses, restaurants and commerces wishing to offer online reservations (appointments and reservations)

Industry/Entity Type

Quindle

Requirements
Must have
• - Easy to integrate with web programming
- light weight visual design. We want something with light tone colors as background
- home page will have a content slider that will show some catch phrases.
- Overall design should be more on the "cartoony" side. Should give a casual, humour and friendly ambiance.

The home page should have these sections:
- a search section for consumers to find local businesses. They will search by specifying "What?" & "Where?"
- a content slider that will cycle through catch phrases and features. Each pane should have an image representative of the text.
- have 4 highlighted sections
- Plimora is great for (list of different businesses types that use plimora)
- Plimora is available for FREE to everyone
- Main features list (accept 24/7 reservations, never reveal your schedule, automatic reminders, marketing campaigns)
- The more you plim, the more you save! (info on our loyalty program that entitles consumers to greater savings and benefits).

One a user logs in, all the certer page info will be replaced by a content div that will allow content to display based on selected menu item
- My Box (opens the main section where all happens. This section should have a design that gives the impression that we're looking in a box)
- My Profile
- My Favorites
Should not have
• - Don't use actual photos of real people, rather opt for sketches and cartoony characters.

```html
<!DOCTYPE html>
<html lang="id">
<head>
<meta charset="utf-8">
<title>Plimora – My Box</title>
<link rel="stylesheet" href="https://fonts.googleapis.com/css2?family=Arimo:wght@400;700&display=swap">
<style>
  :root {
    --bar-dark-top: #3b3b3b;
    --bar-dark-bottom: #161616;
    --cyan-top: #22b4d6;
    --cyan-bottom: #4fe0f4;
    --tab-slate: #3f4d56;
    --tab-light: #f3f3f3;
    --strip: #4b5358;
    --page-bg: #ececec;
    --card-bg: #ffffff;
    --line: #dcdcdc;
    --line-soft: #ececec;
    --text: #222222;
    --muted: #555555;
    --faded: #9a9a9a;
    --navy: #1d3c8c;
    --today-col: #f2f2f2;
    --now-line: #e8806c;
    --accent: #2fc0e0;
    --social: #9fe6f6;
    --footer-bg: #000000;
  }
  * { box-sizing: border-box; margin: 0; padding: 0; }
  html, body { width: 1200px; height: 839px; overflow: hidden; }
  body {
    position: relative;
    font-family: "Arimo", Arial, sans-serif;
    color: var(--text);
    background: var(--page-bg);
  }

  /* top bar */
  .topbar {
    position: absolute; left: 0; top: 0; width: 1200px; height: 68px;
    background: linear-gradient(var(--bar-dark-top), var(--bar-dark-bottom));
  }
  .brand { position: absolute; left: 120px; top: 16px; display: flex; align-items: center; gap: 10px; }
  .brand-mark { width: 30px; height: 30px; background: var(--accent); border-radius: 3px; }
  .brand-name { color: #fff; font-size: 17px; font-weight: 700; letter-spacing: 1px; }
  .search { position: absolute; left: 331px; top: 18px; display: flex; gap: 10px; }
  .search-field {
    width: 286px; height: 28px; border-radius: 5px; border: 0;
    background: #ececec; color: #999; font: 15px "Arimo", Arial, sans-serif;
    padding: 0 9px; line-height: 28px;
  }
  .search-button {
    width: 33px; height: 28px; border-radius: 5px;
    background: linear-gradient(#d4f3fa, #9fdcea);
    display: flex; align-items: center; justify-content: center;
  }
  .main-nav { position: absolute; top: 26px; left: 0; }
  .main-nav a {
    position: absolute; color: #fff; font-size: 11px; font-weight: 700;
    text-decoration: none; white-space: nowrap;
  }

  /* toolbox band */
  .toolbox {
    position: absolute; left: 0; top: 68px; width: 1200px; height: 52px;
    background: linear-gradient(var(--cyan-top), var(--cyan-bottom));
  }
  .toolbox-strip { position: absolute; left: 0; top: 120px; width: 1200px; height: 6px; background: var(--strip); }
  .tab {
    position: absolute; top: 19px; height: 33px;
    display: flex; align-items: center; justify-content: center; gap: 6px;
    background: var(--tab-slate); color: #fff; font-size: 13px; font-weight: 700;
    border-radius: 3px 3px 0 0;
  }
  .tab.is-active { background: linear-gradient(#ffffff, #e6e6e6); color: #777; }
  .session { position: absolute; right: 142px; top: 34px; display: flex; align-items: center; gap: 6px; font-size: 13px; color: #111; }

  /* working card */
  .workspace {
    position: absolute; left: 120px; top: 155px; width: 960px; height: 525px;
    background: var(--card-bg); border: 1px solid #d8d8d8; border-radius: 8px;
    box-shadow: 0 1px 4px rgba(0,0,0,.12);
  }

  /* month picker */
  .month-picker { position: absolute; left: 41px; top: 82px; font-size: 12px; }
  .month-head { display: flex; align-items: center; gap: 6px; font-size: 13px; margin-bottom: 6px; }
  .month-arrows { margin-left: 16px; color: #777; letter-spacing: 10px; font-size: 11px; }
  .month-grid { border-collapse: collapse; }
  .month-grid th, .month-grid td { width: 20px; height: 18px; text-align: center; font-weight: 400; }
  .month-grid th { color: #111; }
  .month-grid .other { color: var(--faded); }
  .month-grid .sunday { color: var(--navy); }
  .month-grid .holiday { font-weight: 700; }
  .month-grid .week-current td { background: #ececec; }
  .month-grid .today span { display: inline-block; border: 1px solid #222; width: 19px; line-height: 16px; }

  /* week planner */
  .week { position: absolute; left: 227px; top: 32px; width: 664px; font-size: 12px; }
  .week-head, .week-allday { display: grid; grid-template-columns: 56px repeat(7, 1fr) 14px; }
  .week-head div { height: 21px; line-height: 21px; text-align: center; color: #444; }
  .week-head .is-today { background: #ececec; font-weight: 700; color: #111; }
  .week-allday div { height: 13px; border: 1px solid var(--line); border-left: 0; }
  .week-allday .tz { border: 0; font-size: 11px; color: #555; line-height: 13px; text-align: center; }
  .week-allday .gap { border: 0; }
  .week-body {
    position: relative; margin-top: 6px; height: 417px; overflow: hidden;
    border: 1px solid var(--line);
    display: grid; grid-template-columns: 56px repeat(7, 1fr) 14px;
  }
  .hours { padding-top: 18px; }
  .hours div { height: 39.4px; font-size: 12px; color: #444; text-align: right; padding-right: 4px; line-height: 12px; margin-top: -6px; padding-top: 0; }
  .hours div:first-child { margin-top: 0; }
  .day {
    border-left: 1px solid var(--line);
    background:
      repeating-linear-gradient(to bottom, transparent 0 18px, var(--line) 18px 19px, transparent 19px 38.4px, var(--line-soft) 38.4px 39.4px);
  }
  .day.is-today { background-color: var(--today-col); }
  .scrollbar { border-left: 1px solid #bbb; position: relative; background: #fafafa; }
  .scrollbar .thumb { position: absolute; left: 0; right: 0; top: 104px; height: 54px; background: #9c9c9c; }
  .scrollbar .arrow { position: absolute; left: 0; right: 0; height: 14px; border-top: 1px solid #bbb; font-size: 8px; text-align: center; line-height: 13px; color: #333; }
  .now-line { position: absolute; left: 477px; width: 84px; top: 267px; height: 2px; background: var(--now-line); }
  .now-marker { position: absolute; left: -4px; top: 264px; width: 0; height: 0; border-top: 4px solid transparent; border-bottom: 4px solid transparent; border-left: 4px solid #c0302a; }

  /* footer */
  .site-footer {
    position: absolute; left: 0; top: 721px; width: 1200px; height: 118px;
    background: var(--footer-bg); color: #fff; font-size: 12px;
  }
  .footer-col { position: absolute; top: 19px; list-style: none; line-height: 17px; }
  .footer-col a { color: #fff; text-decoration: none; }
  .join { position: absolute; left: 422px; top: 19px; }
  .join-links { display: flex; gap: 16px; margin-top: 12px; }
  .join-links a { color: var(--social); font-weight: 700; font-size: 13px; text-decoration: none; }
  .copyright { position: absolute; right: 134px; top: 19px; }
  .copyright a { color: var(--accent); text-decoration: none; }
</style>
</head>
<body>

<header class="topbar">
  <div class="brand"><span class="brand-mark"></span><span class="brand-name">Plimora</span></div>
  <form class="search">
    <div class="search-field">what</div>
    <div class="search-button">
      <svg width="18" height="18" viewBox="0 0 18 18"><circle cx="10.5" cy="7.5" r="5" fill="none" stroke="#111" stroke-width="2.2"/><line x1="7" y1="11" x2="2" y2="16" stroke="#111" stroke-width="3" stroke-linecap="round"/></svg>
    </div>
  </form>
  <nav class="main-nav">
    <a style="left:700px">HOME</a>
    <a style="left:763px">FEATURES</a>
    <a style="left:849px">PRICING</a>
    <a style="left:924px">PURCHASE</a>
    <a style="left:1010px">SUPPORT</a>
  </nav>
</header>

<nav class="toolbox">
  <div class="tab is-active" style="left:122px;width:100px">
    <svg width="11" height="10" viewBox="0 0 11 10"><rect x="0" y="2" width="11" height="8" rx="1" fill="#888"/><rect x="3.5" y="0" width="4" height="3" fill="none" stroke="#888"/></svg>My Box</div>
  <div class="tab" style="left:225px;width:131px">
    <svg width="12" height="11" viewBox="0 0 12 11"><path d="M6 10.5 1 5.5A2.7 2.7 0 0 1 6 2a2.7 2.7 0 0 1 5 3.5Z" fill="#fff"/></svg>My Favorites</div>
  <div class="tab" style="left:359px;width:106px">
    <svg width="11" height="11" viewBox="0 0 11 11"><path d="M1 1 10 10M10 1 1 10M5.5 0v11" stroke="#fff" stroke-width="1.8"/></svg>Settings</div>
  <div class="tab" style="left:468px;width:114px">
    <svg width="9" height="11" viewBox="0 0 9 11"><circle cx="4.5" cy="3" r="2.6" fill="#fff"/><rect x="1" y="6.5" width="7" height="4.5" rx="1" fill="#fff"/></svg>My Profile</div>
  <div class="session">
    <svg width="12" height="14" viewBox="0 0 12 14"><circle cx="6" cy="4" r="3.5" fill="#000"/><path d="M0 14a6 5 0 0 1 12 0Z" fill="#000"/></svg>
    <span>Hi Lauren</span><span>&nbsp;|&nbsp;</span>
    <svg width="14" height="14" viewBox="0 0 14 14"><circle cx="9.5" cy="4.5" r="3.5" fill="#000"/><path d="M7 7 1 13M3 11l2 2" stroke="#000" stroke-width="2"/></svg>
    <span>Logout</span>
  </div>
</nav>
<div class="toolbox-strip"></div>

<main class="workspace">
  <section class="month-picker">
    <div class="month-head"><span style="font-size:8px">&#9660;</span>Desember 2011<span class="month-arrows">&lsaquo;&rsaquo;</span></div>
    <table class="month-grid">
      <tr><th>M</th><th>S</th><th>S</th><th>R</th><th>K</th><th>J</th><th>S</th></tr>
      <tr><td class="other">27</td><td class="other">28</td><td class="other">29</td><td class="other">30</td><td>1</td><td>2</td><td>3</td></tr>
      <tr><td>4</td><td>5</td><td>6</td><td>7</td><td>8</td><td>9</td><td class="sunday">10</td></tr>
      <tr class="week-current"><td>11</td><td>12</td><td>13</td><td>14</td><td class="today"><span>15</span></td><td>16</td><td>17</td></tr>
      <tr><td class="sunday">18</td><td>19</td><td>20</td><td>21</td><td>22</td><td>23</td><td>24</td></tr>
      <tr><td class="holiday">25</td><td>26</td><td>27</td><td>28</td><td>29</td><td>30</td><td>31</td></tr>
      <tr><td class="other">1</td><td class="other">2</td><td class="other">3</td><td class="other">4</td><td class="other">5</td><td class="other">6</td><td class="other">7</td></tr>
    </table>
  </section>

  <section class="week">
    <div class="week-head">
      <div></div><div>Min, 12/11</div><div>Sen, 12/12</div><div>Sel, 12/13</div><div>Rab, 12/14</div><div class="is-today">Kam, 12/15</div><div>Jum, 12/16</div><div>Sab, 12/17</div><div></div>
    </div>
    <div class="week-allday">
      <div class="tz">GMT+07</div><div style="border-left:1px solid var(--line)"></div><div></div><div></div><div></div><div style="background:var(--today-col)"></div><div></div><div></div><div class="gap"></div>
    </div>
    <div class="week-body">
      <div class="hours">
        <div style="margin-top:12px">07.00</div><div>08.00</div><div>09.00</div><div>10.00</div><div>11.00</div><div>12.00</div><div>13.00</div><div>14.00</div><div>15.00</div><div>16.00</div><div>17.00</div>
      </div>
      <div class="day"></div><div class="day"></div><div class="day"></div><div class="day"></div>
      <div class="day is-today"></div><div class="day"></div><div class="day"></div>
      <div class="scrollbar">
        <div class="thumb"></div>
        <div class="arrow" style="bottom:14px">&#9650;</div>
        <div class="arrow" style="bottom:0">&#9660;</div>
      </div>
      <div class="now-line"></div>
      <div class="now-marker"></div>
    </div>
  </section>
</main>

<footer class="site-footer">
  <ul class="footer-col" style="left:131px">
    <li><a>Pricing</a></li><li><a>How it works</a></li><li><a>Priivacy</a></li><li><a>Contact us</a></li><li><a>Terms of service</a></li>
  </ul>
  <ul class="footer-col" style="left:272px">
    <li><a>Getting started</a></li><li><a>FAQ</a></li><li><a>Loyalty program</a></li><li><a>Features</a></li>
  </ul>
  <div class="join">
    <div>JOIN US ON</div>
    <div class="join-links"><a>peeplark</a><a>chatterloom</a><a>crew lattice</a></div>
  </div>
  <div class="copyright">Copyright (c) 2011 <a>Plimora</a>. All rights reserved.</div>
</footer>

</body>
</html>
```